Brit Rock covers band "The Tin Kettles" requires poster for Fernhollow Club Friday March 31st

I want a design for a poster (A3 and A4) and Facebook/Instagram ads.
Primary focus is the band name logo "The Tin Kettles", style as in attached file, followed by tag "Old Skool Brit Rock".
Backdrop to be 60's psychedelic art.
Secondary focus is the venue "The Fernhollow Club"
Supporting text to include:
- 27 Quill Street, Chatswood SYDNEY
- Friday 31st March 2023
- 7:00 pm until late
- Bar sales refreshments
- NO admission fee

```html
<!DOCTYPE html>
<html lang="en">
<head>
<meta charset="utf-8">
<title>The Tin Kettles – The Fernhollow Club</title>
<link rel="stylesheet" href="https://fonts.googleapis.com/css2?family=Montserrat:wght@400;600;700&family=Oswald:wght@600;700&display=swap">
<style>
  :root{
    --page:#e6e3e5;
    --night:#2a0e14;
    --plum:#66203f;
    --wine:#4a1630;
    --magenta:#b01e6c;
    --pink:#d62a7a;
    --sun:#f0df10;
    --ink:#2a0d14;
    --white:#ffffff;
  }
  *{margin:0;padding:0;box-sizing:border-box}
  html,body{width:1200px;height:1200px;overflow:hidden;background:var(--page)}
  .poster{
    position:absolute;left:234px;top:93px;width:718px;height:1015px;
    overflow:hidden;background:var(--night);
    font-family:"Montserrat",Arial,sans-serif;color:var(--white);
  }
  .psychedelic-art{
    position:absolute;inset:0;
    background:
      radial-gradient(circle at 70% 55%, rgba(214,42,122,.75) 0%, rgba(214,42,122,0) 22%),
      radial-gradient(circle at 50% 37%,
        var(--wine) 0%, var(--plum) 30%,
        var(--magenta) 42%, var(--magenta) 47%,
        var(--plum) 56%, var(--wine) 72%, var(--night) 100%);
  }
  .band-name{
    position:absolute;left:0;right:0;top:0;
    font-family:"Oswald",Impact,sans-serif;font-weight:700;color:var(--white);
    text-transform:uppercase;text-align:center;
  }
  .band-name span{position:absolute;left:0;right:0;line-height:1;display:block}
  .band-name .line-1{top:180px;font-size:144px;letter-spacing:1px}
  .band-name .line-2{top:313px;font-size:170px;letter-spacing:1px}
  .tag-band{
    position:absolute;left:275px;right:0;top:495px;height:57px;
    background:var(--sun);display:flex;align-items:center;padding-left:24px;
  }
  .tag-band span{
    font-family:"Oswald",Impact,sans-serif;font-weight:600;font-size:34px;line-height:1;color:var(--ink);
  }
  .details{position:absolute;left:0;right:0;text-align:center;line-height:1}
  .venue{top:724px;font-size:32px;font-weight:700;letter-spacing:1px}
  .address{top:769px;font-size:19px;font-weight:400;letter-spacing:.6px}
  .when{top:810px;font-size:20px;font-weight:700;line-height:26px;letter-spacing:.4px}
  .perk{position:absolute;top:880px;height:48px}
  .perk svg{position:absolute;top:0}
  .perk p{position:absolute;top:2px;white-space:nowrap;font-size:17px;font-weight:600;line-height:24px;letter-spacing:.6px;text-transform:uppercase}
  .perk-bar{left:142px}
  .perk-bar svg{left:0}
  .perk-bar p{left:49px}
  .perk-fee{left:370px}
  .perk-fee svg{left:0}
  .perk-fee p{left:57px}
</style>
</head>
<body>
  <main class="poster">
    <div class="psychedelic-art" role="img" aria-label="1960s psychedelic illustration: swirling magenta and plum waves, an eye in a blue triangle, a blue and pink electric guitar, planets, a yellow star, spiral and lightning bolt"></div>

    <h1 class="band-name"><span class="line-1">The Tin</span><span class="line-2">Kettles</span></h1>

    <div class="tag-band"><span>Old Skool Brit Rock</span></div>

    <h2 class="details venue">THE FERNHOLLOW CLUB</h2>
    <p class="details address">27 Quill Street, Chatswood SYDNEY</p>
    <p class="details when">FRIDAY 31st March 2023<br>7:00 pm until late</p>

    <div class="perk perk-bar">
      <svg width="30" height="44" viewBox="0 0 30 44" aria-hidden="true">
        <path d="M3 4 H27 L24 42 H6 Z" fill="#bfe6ef" stroke="#2a0d14" stroke-width="2.5"/>
        <rect x="9" y="18" width="7" height="7" fill="#fff" stroke="#2a0d14" stroke-width="1.5"/>
        <rect x="15" y="26" width="7" height="7" fill="#fff" stroke="#2a0d14" stroke-width="1.5"/>
      </svg>
      <p>Bar Sales<br>Refreshments</p>
    </div>
    <div class="perk perk-fee">
      <svg width="46" height="46" viewBox="0 0 46 46" aria-hidden="true">
        <circle cx="23" cy="23" r="21" fill="#f0df10" stroke="#2a0d14" stroke-width="2.5"/>
      </svg>
      <p>No Admission<br>Fee</p>
    </div>
  </main>
</body>
</html>
```